Flyer-Design für Tonwerk Bündnis Kreis
Zielgruppe
Die Tonwerk Bündnis Kreis ist ein Netzwerk von Musikunternehmen [Labels, Musikproduzenten, Promotionagenturen, Verlag, Tonstudios, Werbetexter, Videoproduzenten].
Wir möchten Musikern und Bands die notwendigen Kontakte vermitteln, damit sie ihr Release bestmöglich am Markt platzieren können. Die Idee ist es, die Musik der Bands schon ab Produktionsbeginn durch uns und unsere Kooperationspartner zu screenen und einen ganzheitlichen Produktions-, Distributions- und Marketingmix anzubieten - oder auch nur Teilbereiche, je nachdem wie es die Band wünscht.
Entsprechend soll das Leistungsspektrum auf dem Flyer angezeigt werden auf der Vorderseite und auf der Rückseite zum Einsenden von Demos aufgefordert werden.
Zielgruppe:
Unsere Leistungen richten sich an unabhängige Bands und Künstler, die in Eigenverantwortlichkeit agieren und professionelle Vermarktungsstrukturen nutzen möchten, wie auch Künstler und Bands, die eine Zusammenarbeit mit Labels anstreben. Über unsere Kooperationspartner können wir diverse Genre abdecken, Pop, Singer/Songwriter, Jazz, Rock, Dance, Folk etc.
Stil des Flyers: passend zum Stil der Webseite www.tonwerk-buendnis-kreis.de
monochrom, s/w ggfls. eine Farbe zur Hervorhebung
Format: druckfertige PDF wird benötigt, sowie PDF zum eMail Versand
Ich benötige die Datei als jpg druckfertig
Aufgabenstellung
Inhalte:
> Logo der Tonwerk Bündnis Kreis
> Claim: Ihr habt die songs – wir das professionelle Netzwerk
> Gitarrenfoto s/w
> Webseite: www.tonwerk-buendnis-kreis.de
Leistungen auf der Vorderseite des Flyers (Plakativ darstellen):
Großhandelslistung wie Kaufhallen Rolf, Pelikon etc.
Weltweite digitale Distribution
Eure Musik bei Wendoro, KBT etc.
Promotion in Radio, Print, Web, TV
Studioproduktion
Mixing/Mastering
Pressetexte
Musikvideoproduktion
Labelcodes / ISRC Codes
CD Pressung
Artwork / CD Cover
EPK
Rückseite des Flyers:
Bewerbung physische Demos:
Tonwerk Bündnis Kreis
Artist & Repertoire
Lindacher Gasse 41
D-67312 Kesselbrück
Oder
soundfiles und infopaket (Bio, Bandfotos, Konzerthistorie, Discographie)
über cloudserver (z.B. klangbucht, ablagewerk o.ä )

```html
<!DOCTYPE html>
<html lang="de">
<head>
<meta charset="utf-8">
<title>Tonwerk Bündnis Kreis – Flyer</title>
<link href="https://fonts.googleapis.com/css2?family=Ubuntu:wght@300;400;500&display=swap" rel="stylesheet">
<style>
:root{
  --stage:#444444;
  --paper:#ffffff;
  --ink:#3a3a3a;
  --ink-soft:#5a5a5a;
  --photo-dark:#2b2b2b;
}
*{margin:0;padding:0;box-sizing:border-box}
html,body{width:918px;height:1200px;overflow:hidden;background:var(--stage)}
body{position:relative;font-family:"Ubuntu",sans-serif;font-weight:300;color:var(--ink)}
.flyer{position:absolute;left:75px;width:766px;overflow:hidden;background:var(--paper)}
.flyer--front{top:48px;height:539px}
.flyer--back{top:618px;height:539px}

.photo{position:absolute}
.photo--field{inset:0;background:
  radial-gradient(ellipse 30% 45% at 52% 62%, var(--photo-dark) 0%, rgba(43,43,43,.6) 50%, rgba(0,0,0,0) 100%),
  linear-gradient(180deg,#d8d8d8 0%,#b4b4b4 28%,#9a9a9a 55%,#6e6e6e 100%)}
.photo--player{left:0;right:0;top:99px;height:309px;background:
  radial-gradient(ellipse 35% 40% at 38% 60%, #8a8a8a 0%, rgba(90,90,90,.5) 50%, rgba(0,0,0,0) 100%),
  linear-gradient(90deg,#1e1e1e 0%,#3c3c3c 40%,#2a2a2a 70%,#151515 100%)}

.brand-box{position:absolute;left:26px;top:0;width:246px;height:174px;background:var(--paper);
  box-shadow:0 2px 8px rgba(0,0,0,.25);display:flex;flex-direction:column;align-items:center;justify-content:center;gap:10px}
.brand-box__dot{width:40px;height:40px;border-radius:50%;border:3px solid var(--ink-soft)}
.brand-box__name{font-weight:500;font-size:16px;color:var(--ink-soft);letter-spacing:.2px}

.claim{position:absolute;left:27px;top:280px;font-size:25px;line-height:34px;color:var(--ink);font-weight:300}

.service{position:absolute;height:31px;background:var(--paper);font-size:11.5px;line-height:15px;font-weight:400;
  color:var(--ink);display:flex;align-items:center;justify-content:center;text-align:center;
  clip-path:polygon(1% 8%,4% 0,30% 4%,62% 0,97% 3%,100% 0,98% 30%,100% 62%,99% 100%,70% 96%,40% 100%,6% 97%,1% 100%,2% 64%,0 34%)}
.service--a{left:512px;width:192px}
.service--b{left:562px;width:190px}

.web{position:absolute;right:25px;top:25px;font-size:13px;color:var(--ink-soft)}
.coop{position:absolute;left:528px;top:237px;width:204px;height:44px;background:var(--paper);
  font-size:15px;line-height:18px;text-align:center;color:var(--ink);display:flex;align-items:center;justify-content:center;
  clip-path:polygon(1% 6%,5% 0,45% 4%,96% 0,100% 3%,98% 40%,100% 94%,60% 100%,20% 96%,0 100%,2% 55%)}
.coop-text{position:absolute;left:540px;top:295px;width:180px;text-align:center;font-size:11px;line-height:15.5px;color:var(--paper);font-weight:400}

.contact{position:absolute;top:432px}
.contact--post{left:30px}
.contact--cloud{left:346px}
.contact__head{display:flex;align-items:center;gap:9px;font-size:16px;color:var(--ink);font-weight:300}
.contact__head small{font-size:11px;color:var(--ink-soft)}
.contact__body{margin-top:6px;font-size:11.5px;line-height:15.5px;color:var(--ink-soft)}
.contact--post .contact__body{padding-left:26px}
.contact--cloud .contact__body{padding-left:32px}
</style>
</head>
<body>

<section class="flyer flyer--front">
  <div class="photo photo--field" role="img" aria-label="Schwarz-weiß Foto: geöffneter Gitarrenkoffer auf einer Wiese"></div>
  <div class="brand-box"><span class="brand-box__dot"></span><span class="brand-box__name">Tonwerk Bündnis Kreis</span></div>
  <p class="claim">Ihr habt die Songs,<br>wir das professionelle<br>Netzwerk.</p>

  <div class="service service--a" style="top:35px">Großhandelslistung<br>wie Kaufhallen Rolf, Pelikon etc.</div>
  <div class="service service--b" style="top:82px">Weltweite digitale Distribution</div>
  <div class="service service--a" style="top:131px">Eure Musik bei Wendoro, KBT etc.</div>
  <div class="service service--b" style="top:178px">Promotion in Radio,<br>Print, Web, TV</div>
  <div class="service service--a" style="top:227px">Studioproduktion &amp;<br>Mixing/Mastering</div>
  <div class="service service--b" style="top:276px">Pressetexte</div>
  <div class="service service--a" style="top:325px;width:179px">Labelcodes / ISRC Codes</div>
  <div class="service service--b" style="top:374px;left:560px;width:178px">CD Pressung &amp;<br>Artwork / CD Cover</div>
  <div class="service service--a" style="top:423px;width:179px">EPK</div>
  <div class="service service--b" style="top:472px;left:560px;width:178px">Musikvideoproduktion</div>
</section>

<section class="flyer flyer--back">
  <div class="photo photo--player" role="img" aria-label="Schwarz-weiß Foto: Hand greift Akkord auf Gitarrenhals mit Kapodaster"></div>
  <div class="brand-box"><span class="brand-box__dot"></span><span class="brand-box__name">Tonwerk Bündnis Kreis</span></div>
  <p class="web">www.tonwerk-buendnis-kreis.de</p>

  <div class="coop">KOOPERATIONSPARTNER<br>GESUCHT!</div>
  <p class="coop-text">Lust auf eine gemeinsame Zusammenarbeit? Dann meldet euch bei uns – wir suchen noch Kooperationspartner mit der gleichen Leidenschaft für Musik!</p>

  <div class="contact contact--post">
    <div class="contact__head">
      <svg width="17" height="22" viewBox="0 0 17 22" aria-hidden="true"><path d="M8.5 0C3.8 0 0 3.7 0 8.3 0 14 8.5 22 8.5 22S17 14 17 8.3C17 3.7 13.2 0 8.5 0z" fill="#3a3a3a"/><circle cx="8.5" cy="8.3" r="3.2" fill="#fff"/></svg>
      Bewerbung physische Demos
    </div>
    <p class="contact__body">Tonwerk Bündnis Kreis<br>Artist &amp; Repertoire<br>Lindacher Gasse 41<br>D-67312 Kesselbrück</p>
  </div>

  <div class="contact contact--cloud">
    <div class="contact__head">
      <svg width="24" height="16" viewBox="0 0 24 16" aria-hidden="true"><path d="M5 16a5 5 0 0 1-.6-9.9A7 7 0 0 1 17.6 4.4 5.8 5.8 0 0 1 18.5 16z" fill="#3a3a3a"/></svg>
      <span>Über Cloudserver <small>zB Klangbucht, Ablagewerk…</small></span>
    </div>
    <p class="contact__body">Soundfiles &amp; Infopaket (Bio, Bandfotos,<br>Konzerthistorie, Discographie) an<br>info@tonwerk-buendnis-kreis.de</p>
  </div>
</section>

</body>
</html>
```